Seaside commercial building needs a design for a prominent sign

we have bought a small commercial building in a small seaside area. The building was in disrepair and we are rebuilding it and will rent to small businesses. We have a tall sign right on the corner of the area and want to design something special for the sign The address is 1014 and we want to incorporate that into the name, or just have that as the name. The area is called Bonnet Shores which we were going to use and call it Heron Corner. Almost all shops, however use Bonnet in their name. Looking for something unique with a sea-related logo. Elegant, yet welcoming.

```html
<!DOCTYPE html>
<html lang="en">
<head>
<meta charset="utf-8">
<title>Heron Corner – Tenant Sign</title>
<link rel="stylesheet" href="https://fonts.googleapis.com/css2?family=Cormorant+SC:wght@700&display=swap">
<style>
  :root {
    --sign-bg: #1c1c1c;
    --sign-ink: #ffffff;
    --sign-dark: #1c1c1c;
    --sea-teal: #1d7ea0;
  }
  html, body {
    margin: 0;
    padding: 0;
    overflow: hidden;
    background: var(--sign-bg);
  }
  .sign {
    position: relative;
    width: 1200px;
    height: 1200px;
    background: var(--sign-bg);
    color: var(--sign-ink);
    font-family: "Cormorant SC", Georgia, serif;
    font-weight: 700;
    overflow: hidden;
  }
  .address-badge {
    position: absolute;
    left: 550px;
    top: 222px;
    width: 112px;
    height: 68px;
    border-radius: 50%;
    background: var(--sign-ink);
    color: var(--sign-dark);
    display: flex;
    align-items: center;
    justify-content: center;
    font-size: 44px;
    line-height: 1;
  }
  .brand-mark {
    position: absolute;
    left: 521px;
    top: 310px;
    width: 190px;
    height: 190px;
    border-radius: 50%;
    background: var(--sea-teal);
  }
  .building-name {
    position: absolute;
    left: 0;
    width: 1200px;
    top: 372px;
    height: 100px;
    margin: 0;
    display: flex;
    align-items: center;
    justify-content: center;
    font-size: 100px;
    line-height: 1;
    font-weight: 700;
    letter-spacing: 1px;
  }
  .tenant-list {
    list-style: none;
    margin: 0;
    padding: 0;
  }
  .tenant {
    position: absolute;
    left: 0;
    width: 1200px;
    height: 60px;
    display: flex;
    align-items: center;
    justify-content: center;
    font-size: 62px;
    line-height: 1;
    letter-spacing: 1px;
  }
  .tenant--1 { top: 543px; }
  .tenant--2 { top: 632px; }
  .tenant--3 { top: 726px; }
  .tenant--4 { top: 824px; }
  .tenant--5 { top: 924px; }
</style>
</head>
<body>
  <main class="sign">
    <div class="address-badge">1014</div>
    <div class="brand-mark" role="img" aria-label="Sea-themed emblem area behind the building name"></div>
    <h1 class="building-name">Heron Corner</h1>
    <ul class="tenant-list">
      <li class="tenant tenant--1">Marlow Properties</li>
      <li class="tenant tenant--2">Saltmeadow Bakery</li>
      <li class="tenant tenant--3">for lease</li>
      <li class="tenant tenant--4">Name 4</li>
      <li class="tenant tenant--5">Name 5</li>
    </ul>
  </main>
</body>
</html>
```